Online-Marketing-Material für Reinigungsbetrieb
Zielgruppe
Wir sind ein Reinigungsbetrieb mit den Schwerpunkten Treppenhausreinigung und Büroreinigung. Die Zielgruppe sind bei dieser Anzeige Unternehmer.
Aufgabenstellung
Wir wollen eine Aktion starten. 20 Prozent Neukundenrabatt auf Büroreinigungen. Wir sind ein junges, modernes Unternehmen, dass so auch dementsprechend rüber kommen soll.
Gerne mit unseren Farben.

```html
<!DOCTYPE html>
<html lang="de">
<head>
<meta charset="utf-8">
<title>Lippe Glanz – 20 % Rabatt für Neukunden</title>
<link rel="stylesheet" href="https://fonts.googleapis.com/css2?family=Nunito:ital,wght@0,400;0,800;0,900;1,800&display=swap">
<style>
  :root {
    --wall-light: #e6e8ec;
    --wall-mid: #d3d6dd;
    --team-blue: #1f5cc4;
    --team-blue-deep: #1d3f86;
    --trouser-dark: #2b3140;
    --brand-blue: #1a3fd8;
    --brand-teal: #3bbdb0;
    --teal-dark: #2a7a6e;
    --green-start: #3ee83a;
    --green-end: #8cf30c;
    --white: #ffffff;
  }
  html, body {
    margin: 0;
    padding: 0;
    overflow: hidden;
  }
  .ad {
    position: relative;
    width: 1200px;
    height: 519px;
    overflow: hidden;
    font-family: "Nunito", sans-serif;
    background: linear-gradient(180deg, var(--wall-light) 0%, var(--wall-mid) 100%);
  }
  .team-photo {
    position: absolute;
    inset: 0;
  }
  .team-figures {
    position: absolute;
    left: 70px;
    top: 40px;
    width: 750px;
    height: 479px;
    border-radius: 180px 180px 0 0;
    background: linear-gradient(180deg,
      var(--wall-mid) 0%,
      #b8a48e 22%,
      var(--team-blue) 42%,
      var(--team-blue) 66%,
      var(--team-blue-deep) 78%,
      var(--trouser-dark) 100%);
    -webkit-mask-image: linear-gradient(90deg, transparent 0%, #000 8%, #000 92%, transparent 100%);
    mask-image: linear-gradient(90deg, transparent 0%, #000 8%, #000 92%, transparent 100%);
  }
  .brand-band {
    position: absolute;
    left: 0;
    top: 357px;
    width: 640px;
    height: 138px;
    background: linear-gradient(90deg, var(--white) 0%, var(--white) 60%, rgba(255,255,255,0) 100%);
  }
  .brand-mark {
    position: absolute;
    left: 92px;
    top: 382px;
    width: 86px;
    height: 86px;
    background: var(--brand-teal);
  }
  .brand-name {
    position: absolute;
    left: 214px;
    top: 386px;
    margin: 0;
    font-weight: 800;
    font-size: 33px;
    line-height: 32px;
    color: var(--brand-blue);
  }
  .brand-owner {
    position: absolute;
    left: 215px;
    top: 450px;
    margin: 0;
    font-weight: 400;
    font-size: 14px;
    line-height: 1;
    color: var(--brand-teal);
  }
  .offer-shapes {
    position: absolute;
    inset: 0;
    width: 1200px;
    height: 519px;
  }
  .offer-title {
    position: absolute;
    left: 872px;
    top: 100px;
    margin: 0;
    font-weight: 900;
    font-size: 70px;
    line-height: 1;
    color: var(--white);
    text-shadow: 2px 3px 4px rgba(0,0,0,0.3);
    transform: rotate(-1deg);
  }
  .offer-value {
    position: absolute;
    left: 852px;
    top: 232px;
    display: flex;
    align-items: center;
    color: var(--white);
    transform: rotate(-3deg);
  }
  .offer-number {
    font-weight: 900;
    font-size: 140px;
    line-height: 1;
  }
  .offer-unit {
    display: flex;
    flex-direction: column;
    margin-left: 12px;
    font-weight: 900;
    line-height: 0.95;
  }
  .offer-unit .percent { font-size: 56px; }
  .offer-unit .off { font-size: 44px; }
  .offer-audience {
    position: absolute;
    left: 918px;
    top: 388px;
    margin: 0;
    font-weight: 900;
    font-size: 30px;
    line-height: 1.05;
    color: var(--white);
    text-shadow: 1px 2px 3px rgba(0,0,0,0.3);
    transform: rotate(-6deg);
  }
</style>
</head>
<body>
<main class="ad">
  <div class="team-photo" role="img" aria-label="Foto: sechsköpfiges Reinigungsteam in blauen Poloshirts mit Staubsaugern, Sprühflaschen und Tüchern vor heller Wand">
    <div class="team-figures"></div>
  </div>

  <div class="brand-band"></div>
  <span class="brand-mark"></span>
  <p class="brand-name">Lippe<br>Glanz</p>
  <p class="brand-owner">Inh. Marco Vieira</p>

  <svg class="offer-shapes" viewBox="0 0 2226 962" preserveAspectRatio="none" aria-hidden="true">
    <defs>
      <linearGradient id="offer-green" x1="0" y1="0" x2="1" y2="0">
        <stop offset="0" stop-color="var(--green-start)"/>
        <stop offset="1" stop-color="var(--green-end)"/>
      </linearGradient>
    </defs>
    <polygon points="1445,185 2050,25 2060,300 1600,450" fill="var(--teal-dark)"/>
    <polygon points="1445,430 2205,640 2135,810 1760,940 1600,600" fill="var(--teal-dark)"/>
    <polygon points="1535,55 2145,100 2120,430 1590,450" fill="var(--brand-teal)"/>
    <polygon points="1620,640 2100,630 2065,870 1660,920" fill="var(--brand-teal)"/>
    <polygon points="1440,455 2165,425 2205,645 1525,720" fill="url(#offer-green)"/>
  </svg>

  <h1 class="offer-title">Rabatt</h1>
  <div class="offer-value">
    <span class="offer-number">20</span>
    <span class="offer-unit"><span class="percent">%</span><span class="off">OFF</span></span>
  </div>
  <p class="offer-audience">für<br>Neukunden</p>
</main>
</body>
</html>
```